Stickers By Morwen needs a website and logo design

I am starting a home business, "Stickers By Morwen", which I will sell car decals/decals of some sort. I am looking for a creative and professional looking website. I do not want anything too plain/bland, or else I could design it myself. I am up for many options, when it comes to text/colors, and I am not opposed to much. Just nothing too plain. Currently have no logo design to use, may also add this to the project as well. ( I use Wordpress for my site server so it has to be compatible to be used with that website.
Also, I make decals that mainly go on car windows, not as big on car body’s. Also put decals on glassware, and other items. But mainly car windows

Font styles to use
Serif
Sans Serif

Requirements
Nice to have
• some color, not be bland and white everywhere.

```html
<!DOCTYPE html>
<html lang="en">
<head>
<meta charset="utf-8">
<title>Stickers By Morwen</title>
<link rel="stylesheet" href="https://fonts.googleapis.com/css2?family=Montserrat:wght@600;700&family=Oswald:wght@500;600&family=Roboto:wght@400;500;700&display=swap">
<style>
:root{
  --red:#e3141f;
  --red-dark:#c40f18;
  --ink:#1f1f1f;
  --text:#333;
  --muted:#8a8a8a;
  --paper:#ffffff;
  --mist:#efefef;
  --slate:#4a4a4a;
  --night:#2b2d30;
}
*{box-sizing:border-box;margin:0;padding:0}
html,body{width:1200px;height:2844px;overflow:hidden}
body{position:relative;background:var(--mist);font-family:"Roboto",Arial,sans-serif;color:var(--text)}
.abs{position:absolute}
svg{display:block}

/* top bar */
.topbar{left:0;top:0;width:1200px;height:48px;background:var(--red);color:#fff;font-size:15px;font-weight:500}
.topbar .item{top:0;height:48px;display:flex;align-items:center;gap:10px}

/* nav */
.nav{left:0;top:48px;width:1200px;height:77px;background:var(--paper)}
.brand{left:98px;top:0;height:77px;display:flex;align-items:center;font-family:"Montserrat",sans-serif;font-weight:700;font-size:22px;color:var(--red);letter-spacing:.3px}
.menu{left:404px;top:0;height:77px;display:flex;align-items:center;gap:36px;font-size:13.5px;font-weight:500;color:var(--ink);letter-spacing:.3px}
.menu .active{color:var(--red)}
.cart{left:966px;top:0;height:77px;display:flex;align-items:center;gap:10px;font-size:15px;color:var(--ink)}
.cart .ring{width:34px;height:34px;border-radius:50%;border:2px solid var(--red);display:flex;align-items:center;justify-content:center}

/* hero */
.hero{left:0;top:125px;width:1200px;height:455px;background:linear-gradient(90deg,#8d8f91 0%,#9a9c9e 40%,#6b3b3d 62%,#c9161c 78%,#9d1014 100%)}
.hero-title{left:98px;top:255px;font-family:"Montserrat",sans-serif;font-weight:700;font-size:46px;color:#fff;letter-spacing:.5px}
.hero-sub{left:98px;top:333px;font-size:24px;color:#fff}
.btn-ghost{border:2px solid #fff;color:#fff;display:flex;align-items:center;justify-content:center}
.hero-btn{left:98px;top:402px;width:124px;height:49px;font-size:14px;font-weight:500}
.diamond{width:34px;height:34px;border:2px solid currentColor;transform:rotate(45deg);display:flex;align-items:center;justify-content:center}
.diamond svg{transform:rotate(-45deg)}

/* section headings */
.heading{width:1200px;left:0;text-align:center;font-family:"Montserrat",sans-serif;font-weight:700;color:var(--ink)}

/* tabs */
.tabs{left:290px;top:705px;width:620px;height:52px}
.tab{position:absolute;top:0;height:52px;display:flex;align-items:center;justify-content:center;font-size:18px;font-weight:500;color:#fff}

/* product cards */
.card{background:var(--paper);box-shadow:0 0 0 1px #e0e0e0}
.card .photo{position:absolute;left:0;top:0;width:100%}
.card .name{position:absolute;left:0;width:100%;text-align:center;font-size:16px;font-weight:500;color:var(--ink)}
.card .note{position:absolute;left:0;width:100%;text-align:center;font-size:13px;color:var(--muted)}
.btn-dark{background:var(--ink);color:#fff;display:flex;align-items:center;justify-content:center;font-size:13px;font-weight:500}
.btn-red{background:var(--red);color:#fff;display:flex;align-items:center;justify-content:center;font-size:13px;font-weight:500}
.sold{right:-14px;top:-6px;width:58px;height:58px;border-radius:50%;background:var(--red);color:#fff;font-size:11px;font-weight:500;text-align:center;line-height:15px;padding-top:14px}

/* promo band */
.promo{left:0;top:1214px;width:1200px;height:563px;clip-path:polygon(0 44px,50% 44px,100% 0,100% 100%,50% calc(100% - 42px),0 100%)}
.promo-left{left:0;top:0;width:600px;height:563px;background:linear-gradient(180deg,#555 0%,#4a4a4a 60%,#3e3e3e 100%)}
.promo-right{left:600px;top:0;width:600px;height:563px;background:linear-gradient(160deg,#e8212b 0%,var(--red) 50%,#d5121b 100%)}
.promo-h1{left:98px;top:1335px;font-family:"Oswald",sans-serif;font-weight:600;font-size:50px;color:#fff;letter-spacing:-.5px}
.promo-h2{left:98px;top:1422px;font-family:"Oswald",sans-serif;font-weight:600;font-size:38px;color:#fff;letter-spacing:-.5px}
.promo-text{left:98px;top:1496px;width:470px;font-size:16px;line-height:26px;color:#fff}
.promo-btn{left:98px;top:1604px;width:143px;height:59px;font-family:"Oswald",sans-serif;font-weight:500;font-size:22px}
.reviews-title{left:600px;top:1356px;width:600px;text-align:center;font-family:"Montserrat",sans-serif;font-weight:600;font-size:25px;color:#fff}
.quote-badge{left:832px;top:1433px;width:80px;height:80px;border-radius:50%;background:#fff;display:flex;align-items:center;justify-content:center}
.review-text{left:635px;top:1534px;width:480px;text-align:center;font-size:16px;line-height:26px;color:#fff}
.review-name{left:600px;top:1630px;width:600px;text-align:center;font-size:17px;font-weight:500;color:#fff}

/* blog */
.blog-kicker{left:0;top:1805px;width:1200px;text-align:center;font-size:16px;color:var(--text)}
.meta{position:absolute;left:16px;font-size:11.5px;color:var(--red);display:flex;align-items:center;gap:5px}
.post-title{position:absolute;left:16px;font-size:14.5px;font-weight:500;color:var(--ink)}
.post-text{position:absolute;left:16px;width:290px;font-size:12.5px;line-height:22px;color:var(--text)}

/* footer */
.footer{left:0;top:2332px;width:1200px;height:512px;background:linear-gradient(180deg,#3a3c3f 0%,#2d2f32 45%,#4b4d50 100%)}
.phone-badge{left:560px;top:2373px;width:80px;height:80px;border-radius:50%;border:3px solid #fff;display:flex;align-items:center;justify-content:center}
.foot-phone{left:0;top:2484px;width:1200px;text-align:center;font-size:42px;font-weight:500;color:#fff}
.foot-line{left:0;width:1200px;text-align:center;font-size:16px;font-weight:500;color:#fff}
.social{top:2631px;width:46px;height:46px;border-radius:50%;background:#fff}
.social.on{background:var(--red)}
.base{left:0;top:2716px;width:1200px;height:128px;background:var(--red);clip-path:polygon(0 30px,50% 14px,100% 0,100% 100%,0 100%)}
.copy{left:0;top:2795px;width:1200px;text-align:center;font-size:15px;font-weight:500;color:#fff}
</style>
</head>
<body>

<!-- Top bar -->
<div class="abs topbar">
  <div class="abs item" style="left:728px">
    <svg width="18" height="14" viewBox="0 0 18 14"><rect x="1" y="1" width="16" height="12" fill="none" stroke="#fff" stroke-width="1.8"/><path d="M1 1l8 7 8-7" fill="none" stroke="#fff" stroke-width="1.8"/></svg>
    support@stickersbymorwen.com
  </div>
  <div class="abs item" style="left:980px">
    <svg width="15" height="15" viewBox="0 0 24 24"><path d="M6.6 10.8a15.2 15.2 0 006.6 6.6l2.2-2.2c.3-.3.7-.4 1-.2 1.1.4 2.3.6 3.6.6.6 0 1 .4 1 1V20c0 .6-.4 1-1 1A17 17 0 013 4c0-.6.4-1 1-1h3.5c.6 0 1 .4 1 1 0 1.3.2 2.5.6 3.6.1.3 0 .7-.2 1z" fill="#fff"/></svg>
    +180 555 0147
  </div>
</div>

<!-- Navigation -->
<header class="abs nav">
  <div class="abs brand">STICKERS BY MORWEN</div>
  <nav class="abs menu">
    <span class="active">HOME</span><span>OUR PRODUCTS</span><span>STICKERS</span><span>FEATURES</span><span>BLOG</span><span>CONTACT</span>
  </nav>
  <div class="abs cart">
    <span class="ring"><svg width="16" height="16" viewBox="0 0 16 16"><path d="M3 5h10l-1 9H4z" fill="var(--red)"/><path d="M5.5 6V4a2.5 2.5 0 015 0v2" fill="none" stroke="var(--red)" stroke-width="1.5"/></svg></span>
    Cart: 0 Items
  </div>
</header>

<!-- Hero -->
<section class="abs hero" role="img" aria-label="Photo of the front of a red car with a shop sticker on the bumper"></section>
<h1 class="abs hero-title">STICKERS BY MORWEN</h1>
<p class="abs hero-sub">Nemo enim ipsam voluptatem quia voluptas</p>
<div class="abs btn-ghost hero-btn">READ MORE</div>
<div class="abs diamond" style="left:25px;top:334px;color:#fff"><svg width="12" height="12" viewBox="0 0 12 12"><path d="M8 1L3 6l5 5" fill="none" stroke="#fff" stroke-width="1.8"/></svg></div>
<div class="abs diamond" style="left:1137px;top:334px;color:#fff"><svg width="12" height="12" viewBox="0 0 12 12"><path d="M4 1l5 5-5 5" fill="none" stroke="#fff" stroke-width="1.8"/></svg></div>

<!-- Car stickers -->
<h2 class="abs heading" style="top:645px;font-size:24px">CAR STICKERS</h2>
<div class="abs tabs">
  <svg class="abs" style="left:0;top:0" width="620" height="52" viewBox="0 0 620 52">
    <polygon points="24,0 209,0 209,52 24,52 0,26" fill="#111"/>
    <rect x="209" y="0" width="205" height="52" fill="var(--red)"/>
    <polygon points="414,0 596,0 620,26 596,52 414,52" fill="#111"/>
  </svg>
  <div class="tab" style="left:20px;width:189px">BEST OFFERS</div>
  <div class="tab" style="left:209px;width:205px">TOP RATED</div>
  <div class="tab" style="left:414px;width:186px">HOT DEALS</div>
</div>

<div class="abs diamond" style="left:25px;top:963px;color:#333"><svg width="12" height="12" viewBox="0 0 12 12"><path d="M8 1L3 6l5 5" fill="none" stroke="#333" stroke-width="1.8"/></svg></div>
<div class="abs diamond" style="left:1137px;top:963px;color:#333"><svg width="12" height="12" viewBox="0 0 12 12"><path d="M4 1l5 5-5 5" fill="none" stroke="#333" stroke-width="1.8"/></svg></div>

<article class="abs card" style="left:98px;top:800px;width:317px;height:345px">
  <div class="photo" style="height:188px;background:linear-gradient(135deg,#6fa8e6,#1c4fb0 60%,#0e2f73)" role="img" aria-label="Car mirror wrapped in a flag sticker"></div>
  <div class="name" style="top:208px">Nemo Enim Ipsam Voluptatem</div>
  <div class="note" style="top:238px">Sed quia non numquam</div>
  <div class="abs btn-dark" style="left:99px;top:281px;width:118px;height:34px">ADD TO CART</div>
</article>
<article class="abs card" style="left:442px;top:800px;width:317px;height:345px">
  <div class="photo" style="height:188px;background:linear-gradient(135deg,#9fc7f0,#3f7fd0 55%,#e6c24a 85%)" role="img" aria-label="Car mirror with a flag sticker"></div>
  <div class="abs sold">SOLD<br>OUT</div>
  <div class="name" style="top:208px">Nemo Enim Ipsam Voluptatem</div>
  <div class="note" style="top:238px">Sed quia non numquam</div>
  <svg class="abs" style="left:95px;top:281px" width="128" height="34" viewBox="0 0 128 34"><polygon points="10,0 118,0 128,17 118,34 10,34 0,17" fill="var(--red)"/></svg>
  <div class="abs" style="left:95px;top:281px;width:128px;height:34px;display:flex;align-items:center;justify-content:center;color:#fff;font-size:13px;font-weight:500">ADD TO CART</div>
</article>
<article class="abs card" style="left:785px;top:800px;width:317px;height:345px">
  <div class="photo" style="height:188px;background:linear-gradient(135deg,#8c9094,#3c3f42 55%,#1d1f21)" role="img" aria-label="Car windscreen with a price sticker"></div>
  <div class="name" style="top:208px">Nemo Enim Ipsam Voluptatem</div>
  <div class="note" style="top:238px">Sed quia non numquam</div>
  <div class="abs btn-dark" style="left:99px;top:281px;width:118px;height:34px">ADD TO CART</div>
</article>

<!-- Promo band -->
<section class="abs promo">
  <div class="abs promo-left" role="img" aria-label="Dimmed photo of a person applying a car sticker"></div>
  <div class="abs promo-right" role="img" aria-label="Red-tinted photo of a smiling customer"></div>
</section>
<h2 class="abs promo-h1">GREAT STICKER SALES</h2>
<h3 class="abs promo-h2">GET EXCLUSIVE OFFERS!</h3>
<p class="abs promo-text">Nemo enim ipsam voluptatem quia voluptas sit aspernatur aut odit aut fugit, sed quia consequuntur magni dolores eos qui ratione voluptatem sequi nesciunt.</p>
<div class="abs btn-ghost promo-btn">BUY NOW</div>

<h2 class="abs reviews-title">OUR REVIEWS</h2>
<svg class="abs" style="left:762px;top:1455px" width="24" height="40" viewBox="0 0 24 40"><path d="M20 2L4 20l16 18" fill="none" stroke="#fff" stroke-width="2.5"/></svg>
<div class="abs quote-badge"><svg width="30" height="24" viewBox="0 0 30 24"><path d="M0 24V13C0 5 4 1 11 0v5c-3 1-5 3-5 7h5v12zm17 0V13c0-8 4-12 11-13v5c-3 1-5 3-5 7h5v12z" fill="var(--red)"/></svg></div>
<svg class="abs" style="left:958px;top:1455px" width="24" height="40" viewBox="0 0 24 40"><path d="M4 2l16 18L4 38" fill="none" stroke="#fff" stroke-width="2.5"/></svg>
<p class="abs review-text">Nemo enim ipsam voluptatem quia voluptas sit aspernatur aut odit aut fugit, sed quia consequuntur magni dolores eos qui ratione volup tatem sequi nesciunt.</p>
<div class="abs review-name">- Ellis Harper</div>

<!-- Blog -->
<p class="abs blog-kicker">Nemo enim ipsam voluptatem</p>
<h2 class="abs heading" style="top:1838px;font-size:25px">RECENT BLOG POSTS</h2>

<article class="abs card" style="left:98px;top:1907px;width:317px;height:349px">
  <div class="photo" style="height:160px;background:linear-gradient(135deg,#3a3b3d,#6c6e70 50%,#b9161c)" role="img" aria-label="Oval country sticker on the back of a car"></div>
  <div class="meta" style="top:177px">BY ADMIN, <svg width="11" height="10" viewBox="0 0 11 10"><path d="M1 1h9v6H5L2 9V7H1z" fill="var(--red)"/></svg>25, <svg width="11" height="10" viewBox="0 0 11 10"><path d="M5.5 9.5L1 5A2.5 2.5 0 015.5 2 2.5 2.5 0 0110 5z" fill="var(--red)"/></svg>57</div>
  <div class="post-title" style="top:205px">NEMO ENIM IPSAM VOLUPTATEM</div>
  <p class="post-text" style="top:234px">Perspiciatis unde omnis iste natus doxes sitvol tatem accusantium dantiumeaque.</p>
  <div class="abs btn-red" style="left:16px;top:292px;width:100px;height:36px;font-size:12px">READ MORE</div>
</article>
<article class="abs card" style="left:442px;top:1907px;width:317px;height:349px">
  <div class="photo" style="height:160px;background:linear-gradient(135deg,#c9c3b8,#e8551f 45%,#d9381a)" role="img" aria-label="Person wrapping a car panel in orange vinyl"></div>
  <div class="meta" style="top:177px">BY ADMIN, <svg width="11" height="10" viewBox="0 0 11 10"><path d="M1 1h9v6H5L2 9V7H1z" fill="var(--red)"/></svg>25, <svg width="11" height="10" viewBox="0 0 11 10"><path d="M5.5 9.5L1 5A2.5 2.5 0 015.5 2 2.5 2.5 0 0110 5z" fill="var(--red)"/></svg>57</div>
  <div class="post-title" style="top:205px">NEMO ENIM IPSAM VOLUPTATEM</div>
  <p class="post-text" style="top:234px">Perspiciatis unde omnis iste natus doxes sitvol tatem accusantium dantiumeaque.</p>
  <div class="abs btn-dark" style="left:16px;top:292px;width:100px;height:36px;font-size:12px">READ MORE</div>
</article>
<article class="abs card" style="left:785px;top:1907px;width:317px;height:349px">
  <div class="photo" style="height:160px;background:linear-gradient(135deg,#d7d9db,#8f969c 50%,#3b4248)" role="img" aria-label="Person applying film to a car window"></div>
  <div class="meta" style="top:177px">BY ADMIN, <svg width="11" height="10" viewBox="0 0 11 10"><path d="M1 1h9v6H5L2 9V7H1z" fill="var(--red)"/></svg>25, <svg width="11" height="10" viewBox="0 0 11 10"><path d="M5.5 9.5L1 5A2.5 2.5 0 015.5 2 2.5 2.5 0 0110 5z" fill="var(--red)"/></svg>57</div>
  <div class="post-title" style="top:205px">NEMO ENIM IPSAM VOLUPTATEM</div>
  <p class="post-text" style="top:234px">Perspiciatis unde omnis iste natus doxes sitvol tatem accusantium dantiumeaque.</p>
  <div class="abs btn-dark" style="left:16px;top:292px;width:100px;height:36px;font-size:12px">READ MORE</div>
</article>

<!-- Footer -->
<footer class="abs footer" role="img" aria-label="Dark photo of a parking garage with parked cars"></footer>
<div class="abs phone-badge"><svg width="34" height="34" viewBox="0 0 24 24"><path d="M6.6 10.8a15.2 15.2 0 006.6 6.6l2.2-2.2c.3-.3.7-.4 1-.2 1.1.4 2.3.6 3.6.6.6 0 1 .4 1 1V20c0 .6-.4 1-1 1A17 17 0 013 4c0-.6.4-1 1-1h3.5c.6 0 1 .4 1 1 0 1.3.2 2.5.6 3.6.1.3 0 .7-.2 1z" fill="#fff"/></svg></div>
<div class="abs foot-phone">+180 555 0148</div>
<div class="abs foot-line" style="top:2559px">Maple Lane, UK</div>
<div class="abs foot-line" style="top:2584px">info@stickersbymorwen.com</div>
<div class="abs social" style="left:466px" aria-label="Social link"></div>
<div class="abs social on" style="left:523px" aria-label="Social link"></div>
<div class="abs social" style="left:580px" aria-label="Social link"></div>
<div class="abs social" style="left:635px" aria-label="Social link"></div>
<div class="abs social" style="left:690px" aria-label="Social link"></div>
<div class="abs base"></div>
<div class="abs copy">Copyrights © 2017 Stickers By Morwen. All Rights Reserved.</div>

</body>
</html>
```